Exceptional Corporate Business Card Design

Hello,

We need an exceptional corporate business card design based on our logo attached. We require:

1. A Variation for letterpress print
2. Standard size of business card 84mm x 55mm (Artwork 88mm x 59mm)
3. Variation for square business card 65mm x 65mm (Artwork 69mm x 69mm)
4. Variation as a one side print
5. Adobe Illustrator files

The company is in the financial industry, dulvant.com

The logo is attached as vector pdf.
regards

```html
<!DOCTYPE html>
<html lang="en">
<head>
<meta charset="utf-8">
<title>Dulvant Business Card</title>
<link rel="stylesheet" href="https://fonts.googleapis.com/css2?family=Cinzel:wght@400;700&display=swap">
<style>
  :root {
    --bg: #e9e8ec;
    --blue: #3a37a6;
    --blue-deep: #27248a;
    --blue-light: #5a58c4;
    --white: #ffffff;
    --paper-shade: #e3e3ea;
    --ink: #3b3b46;
    --stripe: #2f2f35;
    --ghost: rgba(140, 140, 160, 0.14);
  }
  * { margin: 0; padding: 0; box-sizing: border-box; }
  html, body { width: 1200px; height: 600px; overflow: hidden; }
  body {
    background: var(--bg);
    font-family: "Cinzel", serif;
    position: relative;
  }
  .card {
    position: absolute;
    top: 137px;
    width: 500px;
    height: 327px;
    border-radius: 18px;
    overflow: hidden;
    box-shadow: 0 10px 26px rgba(30, 30, 60, 0.22);
  }
  .card--front { left: 60px; background: linear-gradient(160deg, var(--white) 0%, var(--paper-shade) 100%); }
  .card--back  { left: 640px; background: linear-gradient(150deg, var(--blue-light) 0%, var(--blue) 45%, var(--blue-deep) 100%); }
  .card__art { position: absolute; inset: 0; width: 100%; height: 100%; }

  .wordmark {
    position: absolute;
    display: flex;
    align-items: center;
    gap: 8px;
  }
  .wordmark__dot {
    width: 58px; height: 58px; border-radius: 50%;
    border: 6px solid var(--blue);
    background: var(--white);
  }
  .wordmark__name {
    font-weight: 700;
    font-size: 40px;
    letter-spacing: 1px;
    color: var(--blue);
  }
  .card--front .wordmark { left: 78px; top: 184px; }
  .card--back .wordmark { left: 50%; top: 104px; transform: translateX(-50%); }
  .card--back .wordmark__dot { width: 68px; height: 68px; border-color: var(--white); background: var(--blue); }
  .card--back .wordmark__name { color: var(--white); font-size: 46px; }

  .contact {
    position: absolute;
    right: 34px; top: 34px;
    text-align: right;
    color: var(--ink);
    font-size: 10.5px;
    line-height: 1.7;
  }
  .contact__name { font-size: 15px; font-weight: 700; color: var(--blue); letter-spacing: 0.5px; }
  .contact__role { font-size: 9.5px; margin-bottom: 10px; }
  .contact__address { margin-bottom: 10px; }
  .contact__line { display: flex; justify-content: flex-end; align-items: center; gap: 7px; }
  .contact__line svg { width: 11px; height: 11px; fill: var(--blue); }
</style>
</head>
<body>

<section class="card card--front" aria-label="Business card front">
  <svg class="card__art" viewBox="0 0 500 327" aria-hidden="true">
    <circle cx="390" cy="95" r="118" fill="none" stroke="var(--ghost)" stroke-width="26"/>
    <path d="M0 226 C110 232 240 262 330 327 L0 327 Z" fill="var(--blue)"/>
    <path d="M0 246 C110 252 230 278 300 327 L0 327 Z" fill="var(--blue-deep)" opacity="0.45"/>
    <path d="M0 222 C110 228 240 258 334 327" fill="none" stroke="var(--stripe)" stroke-width="3"/>
  </svg>

  <div class="wordmark">
    <span class="wordmark__dot"></span>
    <span class="wordmark__name">DULVANT</span>
  </div>

  <div class="contact">
    <p class="contact__name">Marlo Hensley</p>
    <p class="contact__role">Founder &amp; CEO</p>
    <p class="contact__address">14-16 Harlow Lane,<br>N2K 3BD, Lyndon, England</p>
    <p class="contact__line">+44 1 555 01870
      <svg viewBox="0 0 12 12"><path d="M2.5 1h2l1 3-1.3 1a6 6 0 0 0 2.8 2.8l1-1.3 3 1v2a1 1 0 0 1-1 1A10 10 0 0 1 1.5 2a1 1 0 0 1 1-1z"/></svg>
    </p>
    <p class="contact__line">office@dulvant.com
      <svg viewBox="0 0 12 12"><path d="M1 2.5h10v7H1z M1.6 3 6 6.5 10.4 3" fill="none" stroke="var(--blue)" stroke-width="1.2"/></svg>
    </p>
    <p class="contact__line">www.dulvant.com
      <svg viewBox="0 0 12 12"><circle cx="6" cy="6" r="4.6" fill="none" stroke="var(--blue)" stroke-width="1.2"/><path d="M1.4 6h9.2M6 1.4c-2.4 2.6-2.4 6.6 0 9.2M6 1.4c2.4 2.6 2.4 6.6 0 9.2" fill="none" stroke="var(--blue)" stroke-width="0.9"/></svg>
    </p>
  </div>
</section>

<section class="card card--back" aria-label="Business card back">
  <svg class="card__art" viewBox="0 0 500 327" aria-hidden="true">
    <defs>
      <linearGradient id="gloss" x1="0" y1="0" x2="1" y2="1">
        <stop offset="0" stop-color="#fff" stop-opacity="0.22"/>
        <stop offset="1" stop-color="#fff" stop-opacity="0"/>
      </linearGradient>
    </defs>
    <path d="M0 0 H300 L120 327 H0 Z" fill="url(#gloss)"/>
    <circle cx="250" cy="250" r="88" fill="none" stroke="rgba(255,255,255,0.08)" stroke-width="22"/>
  </svg>

  <div class="wordmark">
    <span class="wordmark__dot"></span>
    <span class="wordmark__name">DULVANT</span>
  </div>
</section>

</body>
</html>
```